Bref créative
Stationery for an intellectual property right service provider
ZENOLT
Simple
Tarek Baduri
CEO
Lövbergsvägen 7
164 52 Ekmarsby
Solvara
tarek.baduri@zenolt.eu
www.zenolt.eu

```html
<!DOCTYPE html>
<html lang="en">
<head>
<meta charset="utf-8">
<title>ZENOLT Business Card</title>
<link rel="stylesheet" href="https://fonts.googleapis.com/css2?family=Cormorant+Garamond:wght@400;500;600&display=swap">
<style>
  :root {
    --bg: #e9e9ea;
    --white: #ffffff;
    --red: #d51f26;
    --red-dark: #a8111a;
    --red-light: #ec3a3f;
    --ink: #4a4a4c;
    --ink-soft: #7a7a7d;
    --shadow: rgba(0, 0, 0, 0.18);
  }
  * { margin: 0; padding: 0; box-sizing: border-box; }
  html, body {
    width: 1200px;
    height: 1009px;
    overflow: hidden;
    background: var(--bg);
    font-family: "Cormorant Garamond", "Times New Roman", serif;
  }
  .sheet {
    position: relative;
    width: 1200px;
    height: 1009px;
  }
  .card {
    position: absolute;
    left: 220px;
    width: 760px;
    height: 434px;
    border-radius: 26px;
    overflow: hidden;
    box-shadow: 0 14px 30px var(--shadow);
  }
  .card-back {
    top: 60px;
    background: linear-gradient(160deg, var(--red-light) 0%, var(--red) 45%, var(--red-dark) 100%);
  }
  .card-front {
    top: 515px;
    background: var(--white);
  }

  /* Lockup */
  .lockup {
    position: absolute;
    display: flex;
    align-items: center;
  }
  .lockup-name {
    font-weight: 500;
    letter-spacing: 2px;
    line-height: 1;
  }
  .lockup-rule {
    width: 1.5px;
    align-self: stretch;
  }
  .lockup-tagline {
    text-transform: uppercase;
    letter-spacing: 1.2px;
    line-height: 1.25;
    font-weight: 500;
  }
  .card-back .lockup {
    left: 210px;
    top: 178px;
    color: var(--white);
  }
  .card-back .lockup-name { font-size: 62px; }
  .card-back .lockup-rule { background: var(--white); margin: 0 14px; }
  .card-back .lockup-tagline { font-size: 13px; }

  .card-front .lockup {
    left: 44px;
    top: 40px;
    color: var(--ink);
  }
  .card-front .lockup-name { font-size: 44px; }
  .card-front .lockup-rule { background: var(--ink-soft); margin: 0 11px; }
  .card-front .lockup-tagline { font-size: 10px; color: var(--ink-soft); }

  /* Front artwork */
  .front-art {
    position: absolute;
    inset: 0;
  }

  /* Contact */
  .contact {
    position: absolute;
    left: 52px;
    top: 138px;
    list-style: none;
    color: var(--ink);
    font-size: 15px;
    line-height: 23px;
    font-weight: 500;
  }
  .contact li {
    display: flex;
    align-items: center;
    gap: 9px;
  }
  .contact .icon {
    width: 12px;
    height: 12px;
    flex: none;
  }
  .contact .icon-blank { width: 12px; flex: none; }

  /* Holder */
  .holder {
    position: absolute;
    right: 178px;
    top: 262px;
    text-align: right;
  }
  .holder-name {
    font-size: 28px;
    color: var(--red);
    font-weight: 500;
    line-height: 1.1;
  }
  .holder-title {
    font-size: 15px;
    color: var(--ink-soft);
    letter-spacing: 1px;
    margin-top: 2px;
  }
</style>
</head>
<body>
<main class="sheet">

  <section class="card card-back" aria-label="Card back">
    <div class="lockup">
      <span class="lockup-name">ZENOLT</span>
      <span class="lockup-rule"></span>
      <span class="lockup-tagline">Intellectual Property<br>and Rights<br>Advisory</span>
    </div>
  </section>

  <section class="card card-front" aria-label="Card front">
    <svg class="front-art" width="760" height="434" viewBox="0 0 760 434">
      <defs>
        <linearGradient id="redBand" x1="0" y1="0" x2="1" y2="1">
          <stop offset="0" stop-color="#ec3a3f"/>
          <stop offset="1" stop-color="#a8111a"/>
        </linearGradient>
        <linearGradient id="greyBand" x1="0" y1="0" x2="1" y2="0">
          <stop offset="0" stop-color="#f3f3f4"/>
          <stop offset="1" stop-color="#cfcfd2"/>
        </linearGradient>
      </defs>
      <path d="M0 330 C150 420 380 440 590 434 L0 434 Z" fill="url(#greyBand)"/>
      <path d="M760 120 C720 250 650 360 560 434 L760 434 Z" fill="url(#redBand)"/>
      <path d="M760 120 C725 240 670 340 600 410" fill="none" stroke="#ffffff" stroke-opacity="0.35" stroke-width="2"/>
    </svg>

    <div class="lockup">
      <span class="lockup-name">ZENOLT</span>
      <span class="lockup-rule"></span>
      <span class="lockup-tagline">Intellectual Property<br>and Rights<br>Advisory</span>
    </div>

    <ul class="contact">
      <li>
        <svg class="icon" viewBox="0 0 12 12"><path d="M6 0.5a4 4 0 0 0-4 4c0 3 4 7 4 7s4-4 4-7a4 4 0 0 0-4-4z" fill="#d51f26"/><circle cx="6" cy="4.5" r="1.4" fill="#fff"/></svg>
        Lövbergsvägen 7
      </li>
      <li><span class="icon-blank"></span>164 52 Ekmarsby, Solvara</li>
      <li>
        <svg class="icon" viewBox="0 0 12 12"><path d="M2.5 1h2l1 3-1.3 1a7 7 0 0 0 2.8 2.8l1-1.3 3 1v2a1.5 1.5 0 0 1-1.5 1.5A9.5 9.5 0 0 1 1 2.5 1.5 1.5 0 0 1 2.5 1z" fill="#d51f26"/></svg>
        +46 (0)8 555 01 20
      </li>
      <li>
        <svg class="icon" viewBox="0 0 12 12"><rect x="3" y="0.5" width="6" height="11" rx="1.2" fill="#d51f26"/><rect x="4" y="2" width="4" height="6.5" fill="#fff"/></svg>
        +46 (0)70 555 38 14
      </li>
      <li>
        <svg class="icon" viewBox="0 0 12 12"><rect x="0.5" y="2" width="11" height="8" rx="1" fill="#d51f26"/><path d="M1 2.5l5 4 5-4" fill="none" stroke="#fff" stroke-width="1"/></svg>
        tarek.baduri@zenolt.eu
      </li>
      <li>
        <svg class="icon" viewBox="0 0 12 12"><circle cx="6" cy="6" r="5.5" fill="#d51f26"/><path d="M0.5 6h11M6 0.5c-2.5 3-2.5 8 0 11M6 0.5c2.5 3 2.5 8 0 11" fill="none" stroke="#fff" stroke-width="0.8"/></svg>
        www.zenolt.eu
      </li>
    </ul>

    <div class="holder">
      <p class="holder-name">Tarek Baduri</p>
      <p class="holder-title">CEO</p>
    </div>
  </section>

</main>
</body>
</html>
```